'Fern Gully Rest' flyer design

We need a flyer designed to promote our accommodation and boat hire. We have a rustic style self contained accommodation. Please view on Stay a Shed, NZ ID #518073 this has all the photos and information that might be needed. Feel free to contact me if you need/want any of them sending through. We would like to add 1 photo of the boats though so need a space for them. This is a new venture. The only thing we don't have is prices so not sure if we actually put that on or not? Would be nice to add a couple of peoples 'comments' about the place.
Look forward to see what you come up with.
HAS TO BE A6

Thanks Tessa

Target Market(s)

Holiday makers, family, fishermen.

Industry/Entity Type

Accommodation

Requirements
Must have
• Self Contained Accommodation.
Boat Hire, 2 x RW520 with 40hp Korvel outboards, live bait tank, 4 people max. Launch and retrieve if needed.
Vacation Cabins ID #6271, Stay a Shed ID #518073
Ph 07 5143 907
Mob 027 8401 536
Must have bar photo and pizza bar photo.And boat photo
Nice to have
• Fishing photos together and accommodation photos together. Maybe 1 side each.
Some comments would be nice if you think appropriate.

```html
<!DOCTYPE html>
<html lang="en">
<head>
<meta charset="utf-8">
<title>Fern Gully Rest – A6 flyer</title>
<link href="https://fonts.googleapis.com/css2?family=Chicle&family=Gochi+Hand&family=Arimo:ital,wght@0,400;0,700;1,400&display=swap" rel="stylesheet">
<style>
  :root {
    --page: #e9e4dc;
    --red: #d7262e;
    --ink: #232125;
    --panel: #2a2a2c;
    --white: #ffffff;
    --muted: #e6e6e6;
    --sky-top: #8fb0d6;
    --sky-low: #c9d9ea;
    --shed: #5e7d60;
    --bush: #3f6a3a;
  }
  * { box-sizing: border-box; margin: 0; padding: 0; }
  html, body { width: 1200px; height: 824px; overflow: hidden; }
  body { background: var(--page); font-family: "Arimo", Arial, sans-serif; position: relative; }

  .flyer { position: absolute; top: 210px; width: 570px; height: 405px; overflow: hidden; box-shadow: 0 4px 14px rgba(0,0,0,.25); }
  .flyer--front { left: 20px; background: var(--ink); }
  .flyer--back { left: 610px; background: var(--panel); color: var(--white); }

  .brand { font-family: "Chicle", "Arial Black", sans-serif; font-weight: 400; color: var(--red); letter-spacing: 1px; line-height: 1; text-transform: uppercase; }
  .tagline { font-family: "Gochi Hand", cursive; color: var(--white); }

  /* front */
  .hero { position: absolute; left: 0; top: 0; width: 570px; height: 335px;
    background: linear-gradient(180deg, var(--sky-top) 0%, var(--sky-low) 35%, var(--shed) 55%, #4f6a50 80%, var(--bush) 100%); }
  .front-title { position: absolute; top: 12px; left: 0; width: 100%; text-align: center; }
  .front-title .brand { font-size: 50px; }
  .front-title .tagline { font-size: 24px; margin-top: 12px; }

  .features { position: absolute; left: 25px; top: 236px; display: flex; gap: 12px; }
  .feature { width: 122px; }
  .feature__label { background: var(--red); color: var(--white); font-family: "Gochi Hand", cursive; font-size: 14px; text-align: center; height: 18px; line-height: 18px; letter-spacing: .5px; }
  .feature__photo { height: 81px; border: 3px solid var(--white); border-top: 0; }
  .photo-boats { background: linear-gradient(180deg, #6d6f70, #3c3d3f); }
  .photo-bar { background: linear-gradient(180deg, #9aa6ad, #8a6a45); }
  .photo-play { background: linear-gradient(180deg, #b9cde0 0%, #7b9a63 55%, #4f7c3b 100%); }
  .photo-fishing { background: linear-gradient(180deg, #8fb5c9 0%, #4a8b86 60%, #2d6f73 100%); }

  .contact { position: absolute; left: 0; top: 335px; width: 570px; height: 70px; background: var(--ink); color: var(--white); font-size: 15px; line-height: 17px; }
  .contact__divider { position: absolute; left: 0; top: 0; }
  .contact__address { position: absolute; left: 22px; top: 9px; }
  .contact__online { position: absolute; right: 16px; top: 9px; text-align: right; }
  .contact__phones span + span { margin-left: 6px; }

  /* back */
  .back-bloom { position: absolute; left: 130px; top: 60px; width: 320px; height: 320px; border-radius: 50%;
    background: radial-gradient(circle, rgba(185,40,45,.45) 0%, rgba(120,30,35,.25) 45%, rgba(42,42,44,0) 70%); }
  .back-head { position: absolute; left: 16px; top: 14px; display: flex; align-items: baseline; gap: 10px; }
  .back-head .brand { font-size: 29px; }
  .back-head .tagline { font-size: 17px; }

  .thumbs { position: absolute; left: 10px; top: 52px; display: flex; flex-direction: column; gap: 18px; }
  .thumb { width: 118px; height: 70px; border: 3px solid var(--white); border-radius: 6px; }
  .thumb-sunset { background: linear-gradient(180deg, #f2c889 0%, #b0866a 55%, #3c3d38 100%); }
  .thumb-hut { background: linear-gradient(180deg, #b6b8b4, #6a3a2c); }
  .thumb-track { background: linear-gradient(160deg, #2f3a2a, #56704a); }
  .thumb-bbq { background: linear-gradient(180deg, #dfe6dd 0%, #6f9355 60%, #3f6030 100%); }

  .sections { position: absolute; left: 142px; top: 50px; width: 284px; }
  .section { height: 88px; }
  .section h2 { font-family: "Gochi Hand", cursive; font-weight: 400; font-size: 15px; line-height: 16px; color: var(--white); }
  .section p { font-size: 10.5px; line-height: 13px; color: var(--muted); text-align: justify; }
  .perks { list-style: none; display: flex; flex-wrap: wrap; column-gap: 12px; font-size: 10.5px; line-height: 13px; color: var(--muted); }
  .perks li::before { content: ""; display: inline-block; width: 6px; height: 6px; border-radius: 50%; background: var(--white); margin-right: 4px; vertical-align: 1px; }

  .reviews { position: absolute; left: 438px; top: 54px; width: 122px; }
  .review { font-style: italic; font-size: 9.5px; line-height: 12.5px; color: var(--muted); }
  .review p { text-align: justify; }
  .review cite { display: block; text-align: right; margin-top: 10px; }
  .review + .review { margin-top: 30px; }
</style>
</head>
<body>

<section class="flyer flyer--front" aria-label="Flyer front">
  <div class="hero" role="img" aria-label="Photo of the green shed accommodation under a blue sky with bush behind"></div>
  <header class="front-title">
    <h1 class="brand">Fern Gully Rest</h1>
    <p class="tagline">Self contained accommodation in Coromandel Town</p>
  </header>

  <div class="features">
    <div class="feature">
      <div class="feature__label">BOAT HIRE</div>
      <div class="feature__photo photo-boats" role="img" aria-label="Photo of the two hire boats on trailers"></div>
    </div>
    <div class="feature">
      <div class="feature__label">PIZZA &amp; BAR</div>
      <div class="feature__photo photo-bar" role="img" aria-label="Photo of the timber bar and pizza oven"></div>
    </div>
    <div class="feature">
      <div class="feature__label">KID ACTIVITIES</div>
      <div class="feature__photo photo-play" role="img" aria-label="Photo of the playground on the lawn"></div>
    </div>
    <div class="feature">
      <div class="feature__label">FISHING</div>
      <div class="feature__photo photo-fishing" role="img" aria-label="Photo of fishing on the harbour"></div>
    </div>
  </div>

  <footer class="contact">
    <svg class="contact__divider" width="570" height="70" viewBox="0 0 570 70" aria-hidden="true">
      <line x1="344" y1="0" x2="306" y2="70" stroke="var(--white)" stroke-width="5"/>
    </svg>
    <div class="contact__address">
      <div>218 Kauri Road</div>
      <div>Coromandel</div>
      <div class="contact__phones"><span>Ph: 07 5143 907</span><span>Mob: 027 8401 536</span></div>
    </div>
    <div class="contact__online">
      <div>sam.tessa@ferngully.nz</div>
      <div>Vacation Cabins ID# 6271</div>
      <div>Stay a Shed ID# 518073</div>
    </div>
  </footer>
</section>

<section class="flyer flyer--back" aria-label="Flyer back">
  <div class="back-bloom" role="img" aria-label="Soft background photo of a red pohutukawa flower"></div>
  <header class="back-head">
    <h1 class="brand">Fern Gully Rest</h1>
    <p class="tagline">Self contained accommodation in Coromandel Town</p>
  </header>

  <div class="thumbs">
    <div class="thumb thumb-sunset" role="img" aria-label="Photo of the sunset view from the deck"></div>
    <div class="thumb thumb-hut" role="img" aria-label="Photo of the bush hut interior with memorabilia"></div>
    <div class="thumb thumb-track" role="img" aria-label="Photo of the walking track sign"></div>
    <div class="thumb thumb-bbq" role="img" aria-label="Photo of the covered barbecue area"></div>
  </div>

  <div class="sections">
    <article class="section">
      <h2>Relax</h2>
      <p>Make use of our deck out the front of the property accessible for all to use. This overlooks Coromandel township, harbour and beyond with some of the most stunning views and sunsets.</p>
    </article>
    <article class="section">
      <h2>Stay</h2>
      <p>Enjoy our bush hut/fisherman retreat theme with a great collection of memorabilia from the 'old days'.</p>
      <ul class="perks">
        <li>Six private acres</li><li>Kid Friendly</li><li>Pet Friendly</li>
        <li>All linen provided</li><li>No extra charge for cleaning</li>
      </ul>
    </article>
    <article class="section">
      <h2>Explore</h2>
      <p>Take a walk down to the big creek and explore, eels, fresh water crayfish and more. Boat hire: 2 x RW520 with 40hp Korvel outboards, live bait tank, 4 people max. Launch and retrieve if needed.</p>
    </article>
    <article class="section">
      <h2>Wine &amp; Dine</h2>
      <p>The native timber bar with swivel stools is a favourite for many of our visitors. Cook your BBQ undercover, rain or sun and enjoy the peace and quiet. Make use of the covered fish cleaning facilities.</p>
    </article>
  </div>

  <aside class="reviews">
    <blockquote class="review">
      <p>“Thanks for providing such a fantastic place for us to stay. After 6 nights I’m still finding things on the walls and around that, I haven’t noticed yet! The attention to details is amazing. You are a very clever couple and we hope to be back soon. We will definitely be spreading the word on what a great place this is”</p>
      <cite>Maree, Colin, Jess, Ruby &amp; Finn</cite>
    </blockquote>
    <blockquote class="review">
      <p>“Great hosts, super duper amazing beautiful place to stay. Loving the pizzeria- husbands had fun making pizzas &amp; calzone. Thank you so much SAM &amp; Tessa.”</p>
      <cite>Grant, Louise, Ollie, Harper</cite>
    </blockquote>
  </aside>
</section>

</body>
</html>
```